New business Card Design

I'm looking to do a new design for our business cards.

Our Company its called the Garden quarter we are a High end outdoor Design and construction company based out of miami FL

Our Style is elegant, minimalist, Luxury but accessible.

see our Website: www.thegardenquarter-example.com

Attached find our logo as well as some samples the cards that we have for our sister company.

Sample Contact information ( in no particular order):

Marco Ventresca
VP of Sales and Marketing
Marco@thegardenquarter-example.com
555.204.7719
4172 NW 63 AVE Miami Florida, 33199

Designs are Looking Great guys but not quite there yet!

Upload your last few designs between today and Tomorrow. we will be choosing one on Saturday!

Cheers, 

Marco Ventresca
Director Of Marketing 

Hello Guys, 

Sorry we have not made a decision yet.  a lot of cool stuff! just narrowing down our options. 
expect a decision with in a day or 2. 

Marco. 

Target Market(s)

high End Design and construction. Luxurious but accessible

Industry/Entity Type

Construction

Colors

Designer to choose colors to be used in the design.

```html
<!DOCTYPE html>
<html lang="en">
<head>
<meta charset="utf-8">
<title>The Garden Quarter – Business Cards</title>
<link rel="stylesheet" href="https://fonts.googleapis.com/css2?family=Questrial&family=Lora:ital,wght@1,500&display=swap">
<style>
  :root {
    --backdrop: #e4e4e6;
    --card: #f7f7f8;
    --ink: #3a3a3c;
    --ink-soft: #5a5a5e;
    --brand-blue: #1f78c4;
    --brand-green: #4f9a3a;
    --icon: #6c6c70;
    --shadow: rgba(0, 0, 0, 0.16);
  }
  * { box-sizing: border-box; margin: 0; padding: 0; }
  html, body {
    width: 1200px;
    height: 845px;
    overflow: hidden;
    background: var(--backdrop);
    font-family: "Questrial", sans-serif;
    color: var(--ink);
  }
  .stage {
    position: relative;
    width: 1200px;
    height: 845px;
  }
  .card {
    position: absolute;
    top: 272px;
    width: 525px;
    height: 300px;
    background: var(--card);
    border-radius: 22px;
    box-shadow: 0 14px 30px var(--shadow), 0 2px 4px var(--shadow);
    overflow: hidden;
  }
  .card--front { left: 45px; }
  .card--back { left: 630px; }

  /* Front card */
  .identity {
    position: absolute;
    left: 34px;
    top: 62px;
    display: flex;
    align-items: center;
    gap: 14px;
  }
  .identity__mark {
    width: 78px;
    height: 78px;
    border-radius: 50%;
    background: var(--brand-blue);
    flex: none;
  }
  .identity__name {
    font-size: 30px;
    font-weight: 400;
    letter-spacing: 1px;
    line-height: 1;
    white-space: nowrap;
  }
  .identity__first { color: var(--brand-blue); }
  .identity__last { color: var(--brand-green); }
  .identity__title {
    margin-top: 6px;
    font-family: "Lora", serif;
    font-style: italic;
    font-weight: 500;
    font-size: 14px;
    color: var(--ink-soft);
  }
  .contact {
    position: absolute;
    left: 272px;
    top: 158px;
    list-style: none;
    font-size: 11px;
    color: var(--ink-soft);
  }
  .contact__item {
    display: flex;
    align-items: flex-start;
    gap: 8px;
    margin-bottom: 6px;
    line-height: 16px;
    white-space: nowrap;
  }
  .contact__icon {
    width: 16px;
    height: 16px;
    flex: none;
  }
  .corner-accent {
    position: absolute;
    left: 22px;
    top: 200px;
    width: 150px;
    height: 80px;
    border-radius: 8px;
    background: linear-gradient(135deg, rgba(79, 154, 58, 0.18), rgba(31, 120, 196, 0.18));
  }

  /* Back card */
  .brand {
    position: absolute;
    inset: 0;
    display: flex;
    align-items: center;
    justify-content: center;
    gap: 16px;
  }
  .brand__mark {
    width: 62px;
    height: 62px;
    border-radius: 50%;
    background: var(--brand-blue);
    flex: none;
  }
  .brand__name {
    font-size: 30px;
    font-weight: 400;
    letter-spacing: 2px;
    text-transform: uppercase;
    color: var(--ink);
    white-space: nowrap;
  }
</style>
</head>
<body>
<main class="stage">
  <section class="card card--front" aria-label="Business card front">
    <div class="identity">
      <span class="identity__mark" aria-hidden="true"></span>
      <div>
        <h1 class="identity__name"><span class="identity__first">Marco</span> <span class="identity__last">Ventresca</span></h1>
        <p class="identity__title">VP of Sales and Marketing</p>
      </div>
    </div>

    <ul class="contact">
      <li class="contact__item">
        <svg class="contact__icon" viewBox="0 0 16 16"><circle cx="8" cy="8" r="8" fill="var(--icon)"/><rect x="5.5" y="3.5" width="5" height="9" rx="1" fill="none" stroke="#fff" stroke-width="1.2"/></svg>
        555-204-7719
      </li>
      <li class="contact__item">
        <svg class="contact__icon" viewBox="0 0 16 16"><circle cx="8" cy="8" r="8" fill="var(--icon)"/><rect x="4" y="5" width="8" height="6" fill="none" stroke="#fff" stroke-width="1.1"/><path d="M4 5l4 3.5L12 5" fill="none" stroke="#fff" stroke-width="1.1"/></svg>
        Marco@thegardenquarter-example.com
      </li>
      <li class="contact__item">
        <svg class="contact__icon" viewBox="0 0 16 16"><circle cx="8" cy="8" r="8" fill="var(--icon)"/><circle cx="8" cy="8" r="4.2" fill="none" stroke="#fff" stroke-width="1.1"/><path d="M3.8 8h8.4M8 3.8c-2 2.4-2 6 0 8.4M8 3.8c2 2.4 2 6 0 8.4" fill="none" stroke="#fff" stroke-width="0.9"/></svg>
        www.thegardenquarter-example.com
      </li>
      <li class="contact__item">
        <svg class="contact__icon" viewBox="0 0 16 16"><circle cx="8" cy="8" r="8" fill="var(--icon)"/><path d="M8 12.5S4.8 9 4.8 7a3.2 3.2 0 016.4 0c0 2-3.2 5.5-3.2 5.5z" fill="#fff"/><circle cx="8" cy="7" r="1.2" fill="var(--icon)"/></svg>
        <span>4172 NW 63 AVE Miami<br>Florida, 33199</span>
      </li>
    </ul>

    <div class="corner-accent" role="img" aria-label="Decorative green and blue line ornament"></div>
  </section>

  <section class="card card--back" aria-label="Business card back">
    <div class="brand">
      <span class="brand__mark" aria-hidden="true"></span>
      <h2 class="brand__name">The Garden Quarter</h2>
    </div>
  </section>
</main>
</body>
</html>
```